Rack Flyer for Willowcrest Dementia

We need a rack flyer design providing information on services we offer, fees and relevant contact information. Using company branding (logo, font and colours). Must be provided in a format that is easily edited for ongoing use.

For DL size (99 x 210mm)

```html
<!DOCTYPE html>
<html lang="en">
<head>
<meta charset="utf-8">
<title>Willowcrest Dementia – Rack Flyer</title>
<link rel="stylesheet" href="https://fonts.googleapis.com/css2?family=Montserrat:wght@700;800&family=Roboto+Condensed:wght@400;500;700&display=swap">
<style>
  :root {
    --navy: #34305f;
    --orange: #f0a53a;
    --white: #ffffff;
    --ink: #2b2b33;
    --backdrop: #b3b3b3;
    --photo-light: #f1efec;
    --photo-warm: #e3d4bf;
  }
  * { margin: 0; padding: 0; box-sizing: border-box; }
  html, body { width: 1200px; height: 1200px; overflow: hidden; background: var(--backdrop); }
  .flyer {
    position: absolute; left: 348px; top: 64px; width: 504px; height: 1071px;
    background: var(--white); overflow: hidden;
    font-family: "Roboto Condensed", "Arial Narrow", sans-serif; color: var(--ink);
  }
  .hero-photo {
    position: absolute; left: 0; top: 0; width: 504px; height: 660px;
    background:
      radial-gradient(ellipse 55% 40% at 30% 45%, var(--photo-warm), transparent 70%),
      radial-gradient(ellipse 45% 35% at 72% 40%, #f0d79a, transparent 70%),
      linear-gradient(180deg, var(--photo-light) 0%, #ece6de 60%, var(--white) 100%);
  }
  .brand {
    position: absolute; top: 26px; left: 0; width: 504px;
    display: flex; justify-content: center; align-items: center; gap: 10px;
  }
  .brand-dot { width: 34px; height: 34px; border-radius: 50%; background: var(--navy); }
  .brand-name {
    font-family: "Montserrat", sans-serif; font-weight: 700; font-size: 24px; color: var(--navy);
  }
  .headline {
    position: absolute; right: 23px; top: 292px; text-align: right;
    font-family: "Montserrat", sans-serif; font-weight: 800; line-height: 1;
    text-shadow: 0 0 3px var(--white), 0 0 3px var(--white), 0 0 6px var(--white);
  }
  .headline .line { display: block; color: var(--navy); font-size: 43px; }
  .headline .accent { color: var(--orange); font-size: 61px; margin-top: 2px; }
  .intro {
    position: absolute; left: 23px; top: 441px; width: 458px;
    font-size: 12.6px; line-height: 17.4px; text-align: justify; letter-spacing: -0.25px;
  }
  .intro p + p { margin-top: 6px; }
  .lower-band { position: absolute; left: 0; top: 762px; width: 504px; height: 228px; background: var(--navy); }
  .panel { position: absolute; top: 614px; height: 280px; background: var(--orange); }
  .panel-services { left: 23px; width: 279px; }
  .panel-fees { left: 309px; width: 172px; }
  .panel-title {
    height: 31px; background: var(--navy); color: var(--white);
    font-family: "Montserrat", sans-serif; font-weight: 700; font-size: 17px;
    padding-left: 10px; line-height: 33px;
  }
  .panel-list {
    list-style: none; padding: 4px 0 0 27px;
    font-size: 13px; line-height: 18.4px; letter-spacing: -0.35px; color: var(--ink);
  }
  .panel-list li { position: relative; }
  .panel-list li::before {
    content: ""; position: absolute; left: -15px; top: 7px; width: 5px; height: 5px;
    border-radius: 50%; background: var(--ink);
  }
  .coverage {
    position: absolute; left: 23px; top: 904px; width: 458px;
    color: var(--white); font-size: 13px; line-height: 18.6px; letter-spacing: -0.3px; text-align: justify;
  }
  .contact-row { position: absolute; left: 0; top: 990px; width: 504px; height: 50px; }
  .cta-arrows { position: absolute; left: 22px; top: 18px; }
  .cta-text {
    position: absolute; left: 52px; top: 10px; color: var(--navy);
    font-weight: 700; font-size: 13.5px; line-height: 15.5px;
  }
  .phone { position: absolute; left: 278px; top: 11px; display: flex; align-items: center; gap: 13px; }
  .phone-number { color: var(--navy); font-weight: 500; font-size: 25px; }
  .footer-bar { position: absolute; left: 0; top: 1040px; width: 504px; height: 31px; display: flex; }
  .footer-cell { display: flex; align-items: center; gap: 12px; font-weight: 700; font-size: 15px; }
  .footer-email { width: 252px; background: var(--orange); color: var(--navy); padding-left: 23px; }
  .footer-web { width: 252px; background: var(--navy); color: var(--white); padding-left: 28px; }
</style>
</head>
<body>
<main class="flyer">
  <div class="hero-photo" role="img" aria-label="Photo of a smiling older woman with glasses and a younger female caregiver sharing a warm moment"></div>

  <header class="brand">
    <span class="brand-dot"></span>
    <span class="brand-name">Willowcrest Dementia</span>
  </header>

  <h1 class="headline">
    <span class="line">NAVIGATING</span>
    <span class="line">DEMENTIA</span>
    <span class="line accent">TOGETHER</span>
  </h1>

  <section class="intro">
    <p>Navigating a diagnosis of dementia can be daunting. You likely have many questions, and it can be overwhelming trying to figure out where to turn to for answers and help. We want you to know that you are not alone in this journey.</p>
    <p>As the numbers of those living with dementia in Bermuda continue to rise placing greater demands on an already strained health care system, Willowcrest's clinical and evidence based consultation services improve the safety, independence and quality of life of persons with dementia and their caregivers. Our goal is to assist clients to successfully age in place at home with the support of their family caregivers to reduce the overall cost and burden of care for this vulnerable population.</p>
  </section>

  <div class="lower-band"></div>

  <section class="panel panel-services">
    <h2 class="panel-title">Services Offered</h2>
    <ul class="panel-list">
      <li>Comprehensive Dementia Assessment</li>
      <li>Cognitive/Perceptual Screening</li>
      <li>Home Safety Audit (Home modifications and adaptive equipment aids)</li>
      <li>Caregiver Education &amp; Support</li>
      <li>Falls Prevention Strategies</li>
      <li>Personalised Care Planning</li>
      <li>Preparation for future disease progression</li>
      <li>Case Management Support</li>
      <li>Check-in/monitoring visits for clients with limited social support</li>
      <li>Cognitive Stimulation Therapy (group program for individuals with mild-moderate stage dementia)</li>
    </ul>
  </section>

  <section class="panel panel-fees">
    <h2 class="panel-title">Service Fees</h2>
    <ul class="panel-list">
      <li>Initial Consultation $180</li>
      <li>Comprehensive Dementia Assessment $395</li>
      <li>Comprehensive Dementia Assessment &amp; ongoing case management services $720</li>
      <li>Monthly check in/monitoring visits $180</li>
      <li>Cognitive Stimulation Therapy ($500 per term)</li>
    </ul>
  </section>

  <p class="coverage">We are pleased to share that services offered by Willowcrest Dementia are currently covered under Harbourline and Coralpoint health insurance plans. We also have availability of funding support for those in financial need who are unable to afford co-pay, enabling equitable access to these essential care and support services regardless of financial means.</p>

  <section class="contact-row">
    <svg class="cta-arrows" width="20" height="10" viewBox="0 0 20 10" aria-hidden="true">
      <path d="M0 0 L6 5 L0 10Z M7 0 L13 5 L7 10Z M14 0 L20 5 L14 10Z" fill="var(--orange)"/>
    </svg>
    <p class="cta-text">Please feel free to reach out for<br>further information.</p>
    <div class="phone">
      <svg width="20" height="20" viewBox="0 0 20 20" aria-hidden="true">
        <circle cx="10" cy="10" r="10" fill="var(--navy)"/>
        <path d="M7 5.5 L8.6 5.2 L9.4 7.8 L8.4 8.6 Q9.2 10.6 11.2 11.6 L12 10.6 L14.6 11.4 L14.4 13 Q13.8 14.4 12 14 Q7.2 12.6 6 8 Q5.7 6.2 7 5.5Z" fill="var(--white)"/>
      </svg>
      <span class="phone-number">(441) 555 0142</span>
    </div>
  </section>

  <footer class="footer-bar">
    <div class="footer-cell footer-email">
      <svg width="18" height="18" viewBox="0 0 18 18" aria-hidden="true">
        <circle cx="9" cy="9" r="9" fill="var(--navy)"/>
        <rect x="4.5" y="6" width="9" height="6.5" fill="none" stroke="var(--white)" stroke-width="1.1"/>
        <path d="M4.5 6 L9 9.6 L13.5 6" fill="none" stroke="var(--white)" stroke-width="1.1"/>
      </svg>
      <span>info@willowcrestdementia.bm</span>
    </div>
    <div class="footer-cell footer-web">
      <svg width="18" height="18" viewBox="0 0 18 18" aria-hidden="true">
        <circle cx="9" cy="9" r="9" fill="var(--white)"/>
        <g fill="none" stroke="var(--navy)" stroke-width="1">
          <circle cx="9" cy="9" r="5.5"/>
          <ellipse cx="9" cy="9" rx="2.4" ry="5.5"/>
          <path d="M3.5 9 H14.5 M4.3 6.3 H13.7 M4.3 11.7 H13.7"/>
        </g>
      </svg>
      <span>www.willowcrestdementia.bm</span>
    </div>
  </footer>
</main>
</body>
</html>
```